Harbor Ledger BC

I have a baseline business card that I would like to spruce up!

I actually like this business card. I just want to find a way to have all the information below on it and it too look balanced and professional.

Target Market(s)

Small to medium sized companies - Health Insurance Consulting

Industry/Entity Type

Health Insurance

Contact Information for Business Card

The information I would like included on the business card is:

- Harbor Ledger Pacific Title and logo
- Dana Whitlow
- Business title: Principal
- 4312 Alder Crest Rd Suite C-215 Fernvale, WA 98172
- Employee Benefits Consulting & (Wellness Consulting) optional
- dana@harborledgerpac.com
- cell: 425-731-4062

Font styles to use
Other font styles liked:
• I like the font it is currently in but am open to others.

Requirements
Must have
• I like the logo and the color scheme. I even like the layout. I just need to fine tune it!

```html
<!DOCTYPE html>
<html lang="en">
<head>
<meta charset="utf-8">
<title>Harbor Ledger Pacific – Business Card</title>
<link rel="stylesheet" href="https://fonts.googleapis.com/css2?family=Arimo:wght@400;700&display=swap">
<style>
  :root {
    --backdrop: #2b2b2b;
    --card: #f7f7f7;
    --ink: #2e2e2e;
    --ink-soft: #5a5a5a;
    --rule: #8a8a8a;
    --brand-green: #1f8a4c;
  }
  * { box-sizing: border-box; margin: 0; padding: 0; }
  html, body {
    width: 1200px;
    height: 873px;
    overflow: hidden;
    background: var(--backdrop);
    font-family: "Arimo", Arial, sans-serif;
  }
  .stage {
    width: 1200px;
    height: 873px;
    display: flex;
    align-items: center;
    justify-content: center;
  }
  .business-card {
    position: relative;
    width: 840px;
    height: 480px;
    background: var(--card);
    border-radius: 28px;
    color: var(--ink);
  }
  .brand {
    position: absolute;
    left: 60px;
    top: 110px;
    display: flex;
    align-items: center;
    gap: 22px;
  }
  .brand-mark {
    width: 84px;
    height: 84px;
    border-radius: 50%;
    background: var(--brand-green);
  }
  .brand-name {
    font-size: 27px;
    font-weight: 400;
    letter-spacing: 0.5px;
    text-transform: uppercase;
    color: var(--ink);
  }
  .brand-divider {
    position: absolute;
    left: 560px;
    top: 88px;
    width: 1px;
    height: 110px;
    background: var(--rule);
  }
  .service-tagline {
    position: absolute;
    left: 578px;
    top: 96px;
    font-size: 17px;
    line-height: 20px;
    color: var(--ink-soft);
  }
  .contact-rule {
    position: absolute;
    left: 200px;
    right: 50px;
    top: 330px;
    height: 1px;
    background: var(--rule);
  }
  .person {
    position: absolute;
    left: 60px;
    top: 296px;
  }
  .person-name {
    font-size: 24px;
    font-weight: 700;
    letter-spacing: 0.5px;
  }
  .person-title {
    font-size: 19px;
    color: var(--ink-soft);
    margin-top: 2px;
  }
  .office-address {
    position: absolute;
    right: 50px;
    top: 344px;
    text-align: right;
    font-style: normal;
    font-size: 20px;
    line-height: 24px;
    color: var(--ink-soft);
  }
  .direct-contact {
    position: absolute;
    left: 60px;
    top: 392px;
    font-size: 20px;
    line-height: 28px;
    color: var(--ink-soft);
  }
</style>
</head>
<body>
<main class="stage">
  <article class="business-card">
    <div class="brand">
      <span class="brand-mark" aria-hidden="true"></span>
      <span class="brand-name">Harbor Ledger Pacific</span>
    </div>
    <span class="brand-divider" aria-hidden="true"></span>
    <p class="service-tagline">Employee<br>Benefits<br>Consulting</p>

    <div class="person">
      <p class="person-name">Dana Whitlow</p>
      <p class="person-title">Principal</p>
    </div>
    <span class="contact-rule" aria-hidden="true"></span>

    <address class="office-address">
      4312 Alder Crest Rd Suite<br>C-215 Fernvale<br>WA 98172
    </address>

    <div class="direct-contact">
      <p class="phone">425-731-4062</p>
      <p class="email">dana@harborledgerpac.com</p>
    </div>
  </article>
</main>
</body>
</html>
```